Help me design my in store poster to promote our Loan product!

We need a design for a 2 X 3 poster inside our stores to promote our installment loan product. We are called Dorn's Check Cashing, but offer loans inside our stores. We are open to a new logo for Dorn's Loans, and open to any new exciting colors to stand out in the store. We provide short term monthly installment loans, we have monthly payments from 3 - 12 months. Our loans range from $100 - $1,400 with low interest. We ask for ID, consistent source of income, and credit check. We help build credit, and it is fast and easy. We want it to be simple and clean to get people's attention when they are inside our stores. Please help!

UPDATE: The design will be for a 2 X 7 poster now. Less words.

Font styles to use
Other font styles liked:
• Rounded corners with the font

Requirements
Must have
• Bold colors, the words: loans, cash, $100 - $1,400, monthly payments, credit building, quick.
Nice to have
• A new logo, the Dorn's Check Cashing logo added as reference

UPDATE: If we can add a quick slogan : FAST CASH NOW or HELP IS HERE or YOUR CASH IS HERE or LOANS FOR LIVING or LOANS FOR LIFE

A DORN'S FINANCE LOGO that looks similar to the GALEWING logo I attached.

```html
<!DOCTYPE html>
<html lang="en">
<head>
<meta charset="utf-8">
<title>Dorn's Loans – Fast Cash Now 2x7 Banner</title>
<link rel="stylesheet" href="https://fonts.googleapis.com/css2?family=Montserrat:ital,wght@0,800;0,900;1,800;1,900&display=swap">
<style>
  :root {
    --board-grey: #b3b3b3;
    --brand-blue: #0b58bb;
    --brand-blue-light: #1f7ad3;
    --brand-blue-deep: #0a4aa6;
    --brand-red: #e21d26;
    --brand-red-dark: #6e1a20;
    --white: #ffffff;
    --photo-hair: #3a2620;
    --photo-skin: #d9a58c;
    --photo-shirt: #e9bcc8;
  }
  * { margin: 0; padding: 0; box-sizing: border-box; }
  html, body {
    width: 1200px;
    height: 497px;
    overflow: hidden;
    background: var(--board-grey);
    font-family: "Montserrat", sans-serif;
  }
  .banner {
    position: absolute;
    left: 84px;
    top: 96px;
    width: 1030px;
    height: 294px;
    overflow: hidden;
    background: radial-gradient(ellipse at 60% 45%, var(--brand-blue-light) 0%, var(--brand-blue) 55%, var(--brand-blue-deep) 100%);
    box-shadow: 2px 3px 4px rgba(0, 0, 0, 0.35);
  }
  .banner-art {
    position: absolute;
    inset: 0;
    width: 1030px;
    height: 294px;
  }
  .hero-photo {
    position: absolute;
    left: 0;
    top: 0;
    width: 192px;
    height: 294px;
    background: linear-gradient(180deg, var(--photo-hair) 0%, var(--photo-skin) 45%, var(--photo-shirt) 100%);
  }
  .headline {
    font-family: "Montserrat", sans-serif;
    font-weight: 900;
    font-style: italic;
    font-size: 78px;
    letter-spacing: -3px;
    fill: var(--white);
  }
  .benefit {
    font-family: "Montserrat", sans-serif;
    font-weight: 800;
    font-style: italic;
    font-size: 26px;
    letter-spacing: -1px;
    fill: var(--white);
  }
  .loan-range {
    font-family: "Montserrat", sans-serif;
    font-weight: 800;
    font-style: italic;
    font-size: 13px;
    letter-spacing: 0;
    fill: var(--white);
  }
  .cta-label {
    font-family: "Montserrat", sans-serif;
    font-weight: 800;
    font-size: 18px;
    fill: var(--white);
  }
  .brand-name {
    font-family: "Montserrat", sans-serif;
    font-weight: 900;
    font-size: 24px;
    fill: var(--brand-red);
  }
</style>
</head>
<body>
  <div class="banner">
    <svg class="banner-art" viewBox="0 0 1030 294" xmlns="http://www.w3.org/2000/svg">
      <defs>
        <linearGradient id="ribbonFill" x1="0" y1="0" x2="1" y2="0">
          <stop offset="0" stop-color="var(--brand-red-dark)"/>
          <stop offset="0.55" stop-color="var(--brand-red)"/>
          <stop offset="1" stop-color="var(--brand-red)"/>
        </linearGradient>
        <linearGradient id="ribbonLowerFill" x1="0" y1="0" x2="1" y2="0">
          <stop offset="0" stop-color="var(--brand-red)"/>
          <stop offset="0.6" stop-color="var(--brand-red)"/>
          <stop offset="1" stop-color="#a01820"/>
        </linearGradient>
        <filter id="textShadow" x="-10%" y="-10%" width="130%" height="140%">
          <feDropShadow dx="2" dy="3" stdDeviation="1.5" flood-color="#000" flood-opacity="0.55"/>
        </filter>
      </defs>

      <!-- headline ribbons -->
      <polygon class="ribbon-fold" points="499,209 520,209 535,270 484,270 499,253" fill="#8c161c"/>
      <polygon class="ribbon-upper" points="187,27 497,27 463,104 496,175 187,175" fill="url(#ribbonFill)"/>
      <polygon class="ribbon-lower" points="266,184 499,184 499,253 266,253 289,219" fill="url(#ribbonLowerFill)"/>

      <!-- speed lines -->
      <g class="speed-lines" fill="var(--white)">
        <polygon points="205,58 250,55 250,59"/>
        <polygon points="212,67 248,64 248,68"/>
        <polygon points="208,76 245,73 245,77"/>
      </g>

      <!-- headline -->
      <g filter="url(#textShadow)">
        <text class="headline" x="236" y="95">FAST</text>
        <text class="headline" x="254" y="162">CA$H</text>
        <text class="headline" x="287" y="246">NOW!</text>
      </g>

      <!-- benefits -->
      <g class="check" transform="translate(541,56)">
        <circle r="10.5" fill="var(--brand-red)" stroke="var(--white)" stroke-width="1.5"/>
        <polyline points="-5,0 -1.5,4 5,-4" fill="none" stroke="var(--white)" stroke-width="2.6" stroke-linecap="round" stroke-linejoin="round"/>
      </g>
      <g class="check" transform="translate(541,132)">
        <circle r="10.5" fill="var(--brand-red)" stroke="var(--white)" stroke-width="1.5"/>
        <polyline points="-5,0 -1.5,4 5,-4" fill="none" stroke="var(--white)" stroke-width="2.6" stroke-linecap="round" stroke-linejoin="round"/>
      </g>
      <g filter="url(#textShadow)">
        <text class="benefit" x="564" y="67">MONTHLY</text>
        <text class="benefit" x="564" y="100">INSTALLMENT LOAN</text>
        <text class="benefit" x="564" y="144">PAYMENTS UP TO</text>
        <text class="benefit" x="566" y="179">12 MONTHS</text>
      </g>

      <!-- call to action -->
      <rect class="cta-button" x="565" y="220" width="164" height="31" rx="15.5" fill="var(--brand-red)" stroke="var(--white)" stroke-width="1.5"/>
      <text class="cta-label" x="647" y="242" text-anchor="middle">APPLY NOW!</text>
      <text class="loan-range" x="567" y="277" filter="url(#textShadow)">$100 - $1,400 LOANS · CREDIT BUILDING</text>

      <!-- brand side stripes and panel -->
      <path class="stripe-white" d="M846,0 L870,0 C920,110 905,220 905,294 L895,294 C900,200 900,100 846,0 Z" fill="var(--white)"/>
      <path class="stripe-red" d="M870,0 L900,0 C935,100 912,220 912,294 L905,294 C905,220 920,110 870,0 Z" fill="var(--brand-red)"/>
      <path class="brand-panel" d="M918,0 C945,100 920,200 916,294 L1030,294 L1030,0 Z" fill="var(--white)"/>

      <!-- brand name -->
      <text class="brand-name" x="977" y="182" text-anchor="middle">DORN'S</text>
      <text class="brand-name" x="977" y="210" text-anchor="middle">LOANS</text>
    </svg>

    <div class="hero-photo" role="img" aria-label="Photo of a smiling woman holding a fan of hundred-dollar bills"></div>
  </div>
</body>
</html>
```